依頼概要
毎年、全社員の名前、顔写真、誕生日、ひと言コメントを掲載した冊子を作成しています。これまでは表紙について、自社でデザインを実施していましたがロゴ等を並列のするのみのデザイン性に乏しいものでした。
この名鑑を社員一人一人が手にしたときに、ワクワクする!すぐに読みたい!テンションがUPする!というようなデザインにしたいと考えています。
スピード重視ですので、あまり凝ったデザインでなくても良いかなと考えています。

なお、名鑑は2法人(社会福祉法人光彩苑と学校法人桐谷学園)で共同で使用いたします。

法人の理念は、
For The Community~地域のために私たちができること~

となります。

法人のイメージカラーは、オレンジと緑です。

素晴らしいご提案を頂戴できるように楽しみにしています。

```html
<!DOCTYPE html>
<html lang="ja">
<head>
<meta charset="utf-8">
<title>For The Community スタッフ名鑑 2016</title>
<link rel="stylesheet" href="https://fonts.googleapis.com/css2?family=M+PLUS+Rounded+1c:wght@500;800&family=Space+Mono:wght@700&display=swap">
<style>
  :root {
    --orange-light: #ffc23a;
    --orange-mid: #f98a1c;
    --orange-deep: #e9531a;
    --band: #e8641b;
    --white: #ffffff;
    --ink: #2b1a0e;
  }
  html, body {
    margin: 0;
    padding: 0;
    width: 854px;
    height: 1200px;
    overflow: hidden;
    background: var(--white);
  }
  .cover {
    position: relative;
    width: 854px;
    height: 1200px;
    overflow: hidden;
  }
  .cover-burst {
    position: absolute;
    inset: 0;
    background: radial-gradient(circle at 52% 52%, var(--orange-light) 0%, var(--orange-mid) 45%, var(--orange-deep) 100%);
  }
  .cover-title {
    position: absolute;
    left: 0;
    top: 0;
    width: 854px;
    height: 1200px;
  }
  .title-latin {
    font-family: "Space Mono", monospace;
    font-weight: 700;
    fill: var(--white);
  }
  .title-jp {
    font-family: "M PLUS Rounded 1c", sans-serif;
    font-weight: 800;
    fill: var(--white);
  }
  .motto-band {
    position: absolute;
    left: 70px;
    top: 746px;
    width: 710px;
    height: 54px;
    background: var(--band);
    display: flex;
    align-items: center;
    justify-content: center;
    font-family: "M PLUS Rounded 1c", sans-serif;
    font-weight: 800;
    font-size: 33px;
    color: var(--white);
    letter-spacing: 0.02em;
    white-space: nowrap;
  }
  .issuers {
    position: absolute;
    right: 128px;
    top: 1068px;
    font-family: "M PLUS Rounded 1c", sans-serif;
    color: var(--ink);
    text-align: left;
  }
  .issuer {
    display: flex;
    align-items: baseline;
    gap: 10px;
    line-height: 1.35;
  }
  .issuer-type {
    font-weight: 500;
    font-size: 13px;
    width: 86px;
    text-align: justify;
    text-align-last: justify;
  }
  .issuer-name {
    font-weight: 800;
    font-size: 21px;
    letter-spacing: 0.04em;
  }
</style>
</head>
<body>
  <main class="cover">
    <div class="cover-burst" role="img" aria-label="オレンジの放射状バーストと紙吹雪の背景"></div>

    <svg class="cover-title" viewBox="0 0 854 1200" aria-label="For The Community スタッフ名鑑 2016">
      <text class="title-latin" x="40" y="530" font-size="150" textLength="232" lengthAdjust="spacingAndGlyphs">For</text>
      <text class="title-jp" x="295" y="440" font-size="66" textLength="290" lengthAdjust="spacingAndGlyphs">スタッフ名鑑</text>
      <text class="title-latin" x="40" y="640" font-size="150" textLength="232" lengthAdjust="spacingAndGlyphs">The</text>
      <text class="title-latin" x="445" y="640" font-size="150" textLength="400" lengthAdjust="spacingAndGlyphs">2016</text>
      <text class="title-latin" x="40" y="742" font-size="150" textLength="805" lengthAdjust="spacingAndGlyphs">Community</text>
    </svg>

    <div class="motto-band">地域の皆さまのために私たちが出来ること</div>

    <footer class="issuers">
      <div class="issuer">
        <span class="issuer-type">社会福祉法人</span>
        <span class="issuer-name">光彩苑</span>
      </div>
      <div class="issuer">
        <span class="issuer-type">学校法人</span>
        <span class="issuer-name">桐谷学園</span>
      </div>
    </footer>
  </main>
</body>
</html>
```